Thread and Bloom relaunch: brand, logo and website redesign

Thread and Bloom www.threadandbloom.example is relaunching to focus on empowering style advice, e books and courses.
We need a new logo, brand identity and website which reflects this change.
The structure of the site and pages have been completed http://dev1.threadandbloom.example/
but we need to update the brand look and feel
Please read the full brief, uploaded, before submitting your designs.
Updates

Need extra days to review

Target Market(s)

Women, primarily aged 28-45, English speaking USA and UK
Ambitious and determined. Looking for solutions. Open to self-improvement.
Maybe not as confident with style and body image as other parts of their life.

Logo Text

Brand name Thread and Bloom Strapline version 1: Step into your finest self Strapline version 2: Rise further Logo/graphical icon for use with/without text

Number of Pages Required

3 page

Font styles to use
Sans Serif

Requirements
Must have
• 1. Web designs for home page, a channel page and advice page (see attached brief)
Web designs must be consistent with new website design navigation, and page structure http://dev1.threadandbloom.example/
2. Web style guide to include colour palettes/system; web fonts, icons, illustrations and guidelines/examples free stock photography. see Mindmap upload for example of colour pallette we like.
Nice to have
• Ebook front covers
Quiz promotions
Course promotions
Other web pages
Social media pages eg Facebook, Instagram,Twitter
Should not have
• Paid photography or photos where don’t have the rights

```html
<!DOCTYPE html>
<html lang="en">
<head>
<meta charset="utf-8">
<title>Thread and Bloom — Courses</title>
<link href="https://fonts.googleapis.com/css2?family=Figtree:wght@400;500;600&family=Marcellus&family=Caveat:wght@600&display=swap" rel="stylesheet">
<style>
:root{
  --orange:#fb8530;
  --green:#3fd84c;
  --navy:#1b2a4e;
  --ink:#1c2541;
  --soft:#f7f8fb;
  --white:#ffffff;
  --photo-warm:#8a6a52;
  --photo-cool:#c9ced6;
  --photo-skin:#b49a88;
}
*{margin:0;padding:0;box-sizing:border-box}
html,body{width:672px;height:1200px;overflow:hidden}
body{position:relative;background:var(--white);font-family:'Figtree',sans-serif;color:var(--ink)}
.abs{position:absolute}
.band{position:absolute;left:0;width:672px;background:var(--soft)}
.brand{position:absolute;left:49px;text-align:center;width:106px}
.brand-mark{width:16px;height:16px;border-radius:50%;background:var(--orange);margin:0 auto 4px}
.brand-name{font-family:'Figtree',sans-serif;font-weight:400;font-size:12.5px;color:var(--orange);white-space:nowrap;letter-spacing:.2px}
.brand-tag{font-size:5px;color:var(--orange);letter-spacing:.3px;text-transform:uppercase;margin-top:2px}
.nav{position:absolute;top:44px;left:0;font-size:7.5px;color:var(--ink)}
.nav a{position:absolute;white-space:nowrap;color:inherit;text-decoration:none}
.cart{position:absolute;left:598px;top:38px;width:24px;height:24px;border-radius:50%;background:var(--navy)}
.cart-count{position:absolute;left:613px;top:36px;width:9px;height:9px;border-radius:50%;background:var(--orange);color:#fff;font-size:5px;text-align:center;line-height:9px}
.kicker{font-family:'Marcellus',serif;font-size:14px;left:49px;top:139px}
.headline{font-family:'Marcellus',serif;font-size:38px;color:var(--green);left:45px;top:156px;line-height:1}
.script{font-family:'Caveat',cursive;font-size:12px;color:var(--green);left:532px;top:150px;transform:rotate(-2deg)}
.photo{position:absolute}
.play{position:absolute;width:30px;height:30px;border-radius:50%;background:#fff}
.play::after{content:"";position:absolute;left:12px;top:9px;border-left:9px solid var(--orange);border-top:6px solid transparent;border-bottom:6px solid transparent}
.card-title{position:absolute;font-family:'Marcellus',serif;font-size:22.5px;color:var(--ink);white-space:nowrap}
.card-text{position:absolute;font-size:8px;line-height:19.5px;width:250px}
.btn{position:absolute;height:34px;width:96px;font-size:6.5px;font-weight:600;text-align:center;line-height:34px}
.btn-fill{background:var(--orange);color:#fff}
.btn-line{border:1px solid var(--orange);color:var(--orange);background:#fff}
.badge{left:49px;top:707px;width:74px;height:22px;border:1px solid var(--orange);color:var(--orange);font-size:6.5px;font-weight:600;line-height:20px;text-align:center}
.feature-title{left:48px;top:737px;font-family:'Marcellus',serif;font-size:27px;line-height:34px}
.feature-text{left:47px;top:815px;font-size:6.5px;line-height:17px;width:240px}
.foot-head{position:absolute;top:1015px;font-size:7px;font-weight:600}
.foot-list{position:absolute;font-size:7px;line-height:16.3px;list-style:none}
.phone-box{left:350px;top:1073px;width:106px;height:21px;background:#fff;border-radius:3px;box-shadow:0 2px 6px rgba(0,0,0,.06)}
.social{position:absolute;top:1041px;width:25px;height:25px;border-radius:50%}
.legal{left:0;width:672px;text-align:center;font-size:5.5px}
</style>
</head>
<body>
<div class="band" style="top:0;height:328px"></div>
<div class="band" style="top:656px;height:283px"></div>
<div class="band" style="top:953px;height:247px"></div>

<header>
  <div class="brand" style="top:29px">
    <div class="brand-mark"></div>
    <div class="brand-name">THREAD AND BLOOM</div>
    <div class="brand-tag">Step into your finest self</div>
  </div>
  <nav class="nav">
    <a style="left:307px">Advice</a><a style="left:350px">Courses</a><a style="left:397px">Quizzes</a>
    <a style="left:444px">Ebooks</a><a style="left:488px">About</a><a style="left:528px">Blog</a>
  </nav>
  <svg class="abs" style="left:572px;top:46px" width="9" height="9" viewBox="0 0 9 9"><circle cx="3.6" cy="3.6" r="2.8" fill="none" stroke="#1c2541" stroke-width="1"/><line x1="5.6" y1="5.6" x2="8.5" y2="8.5" stroke="#1c2541" stroke-width="1"/></svg>
  <div class="cart"><svg style="position:absolute;left:7px;top:6px" width="10" height="11" viewBox="0 0 10 11"><rect x="1" y="3.5" width="8" height="7" fill="none" stroke="#fff" stroke-width="1"/><path d="M3 3.5V2.5a2 2 0 0 1 4 0v1" fill="none" stroke="#fff" stroke-width="1"/></svg></div>
  <div class="cart-count">1</div>
</header>

<section>
  <div class="abs kicker">Our Latest</div>
  <h1 class="abs headline" style="font-weight:400">Courses</h1>
  <div class="abs script">Latest Bestselling Courses</div>
  <svg class="abs" style="left:509px;top:166px" width="22" height="28" viewBox="0 0 22 28"><path d="M19 2C10 3 5 10 6 24" fill="none" stroke="#3fd84c" stroke-width="1"/><path d="M3 21l3 4 3-4" fill="none" stroke="#3fd84c" stroke-width="1"/></svg>

  <div class="photo" role="img" aria-label="Wardrobe rail with colourful dresses and folded clothes" style="left:49px;top:235px;width:269px;height:190px;background:linear-gradient(135deg,#4a4038,var(--photo-warm),#3a3530)"></div>
  <div class="play" style="left:169px;top:315px"></div>
  <div class="photo" role="img" aria-label="Flat lay of knitted hat, jumper, jeans, watch and tulips" style="left:353px;top:236px;width:270px;height:189px;background:linear-gradient(135deg,#e4e6ea,var(--photo-cool),#9fb0c4)"></div>
  <div class="play" style="left:473px;top:315px"></div>

  <h2 class="card-title" style="left:52px;top:454px;font-weight:400">Colour for clothes course</h2>
  <p class="card-text" style="left:52px;top:491px">Colour is individual, natural, magnetic, influential, emotional, therapeutic and joyful and the emotions it stirs are a vital part of a woman’s beauty and charm.</p>
  <div class="btn btn-fill" style="left:49px;top:569px">Register</div>
  <div class="btn btn-line" style="left:160px;top:569px">Learn more</div>

  <h2 class="card-title" style="left:353px;top:454px;font-weight:400">Minimal clothing course</h2>
  <p class="card-text" style="left:353px;top:491px;width:240px">The clothes which will flatter you best will depend on your body shape. Today the choice of clothes is so varied that there’s something for everyone.</p>
  <div class="btn btn-fill" style="left:353px;top:569px">Register</div>
  <div class="btn btn-line" style="left:464px;top:569px">Learn more</div>
</section>

<section>
  <div class="abs badge">•&nbsp; NEW COURSE</div>
  <h2 class="abs feature-title" style="font-weight:400">Latest Marisa<br>Lindqvist video course</h2>
  <p class="abs feature-text">Marisa Lindqvist’s clean cut, figure flattering and empowering dresses reflect contemporary classics and the latest trends.</p>
  <div class="btn btn-fill" style="left:47px;top:861px;width:91px;height:32px;line-height:32px;font-size:7px;font-weight:500">Register</div>
  <div class="btn" style="left:146px;top:861px;width:91px;height:32px;line-height:30px;font-size:7px;font-weight:500;border:1px solid var(--ink)">Learn more</div>
  <div class="photo" role="img" aria-label="Video still of the course presenter beside a pink garment" style="left:344px;top:701px;width:299px;height:189px;background:linear-gradient(90deg,#9e8a7c,var(--photo-skin) 55%,#e9b4c2)"></div>
  <div class="play" style="left:482px;top:784px;width:22px;height:22px"></div>
</section>

<footer>
  <div class="brand" style="top:1007px">
    <div class="brand-mark"></div>
    <div class="brand-name">THREAD AND BLOOM</div>
    <div class="brand-tag">Step into your finest self</div>
  </div>
  <div class="foot-head" style="left:210px">Navigation</div>
  <ul class="foot-list" style="left:210px;top:1029px"><li>Home</li><li>Advice</li><li>About</li><li>Contact</li></ul>
  <div class="foot-head" style="left:280px">Product</div>
  <ul class="foot-list" style="left:280px;top:1029px"><li>Courses</li><li>Quizzes</li><li>Ebooks</li><li>Blog</li></ul>
  <div class="foot-head" style="left:350px">Place</div>
  <div class="abs" style="left:350px;top:1032px;font-size:7px;line-height:15px">12 Harbour Lane, Riverton 4100<br>contact@threadandbloom.example</div>
  <div class="abs phone-box">
    <svg class="abs" style="left:7px;top:6px" width="9" height="9" viewBox="0 0 9 9"><circle cx="4.5" cy="4.5" r="4.5" fill="#2cc7d4"/><path d="M3 2.5l1 1-.5.8a3 3 0 0 0 1.2 1.2l.8-.5 1 1-.6.8C4.5 6.6 2.6 4.8 2.4 3.1z" fill="#fff"/></svg>
    <span class="abs" style="left:20px;top:7px;font-size:3.5px">Call us on</span>
    <span class="abs" style="left:40px;top:6px;font-size:6px;font-weight:600;letter-spacing:1.3px">0500-123-456</span>
  </div>
  <div class="foot-head" style="left:501px">Social Media</div>
  <div class="social" style="left:501px;background:var(--navy)" aria-label="Social profile"></div>
  <div class="social" style="left:535px;background:var(--orange);box-shadow:0 3px 8px rgba(251,133,48,.35)" aria-label="Social profile"></div>
  <div class="social" style="left:567px;background:var(--navy)" aria-label="Social profile"></div>
  <div class="abs legal" style="top:1162px;font-size:6px">© Thread and Bloom Company - All Rights Reserved</div>
  <div class="abs legal" style="top:1175px;font-size:4.5px">Terms &amp; Conditions | Privacy Policy | | Contact Us</div>
</footer>
</body>
</html>
```